Packaging Design Job - Baby Diaper Rash Cream and Wipes Packaging Concepts Needed

Hello, Our baby brand “Mavory” is launching 2 new products – a Diaper Rash Cream and Diaper Wipes – and would like some creative design concepts for our product packaging.Mavory is a pharmaceutical brand that specializes in baby products. We are a mid – premium priced brand with a focus on targeting mothers between the ages of 18 – 35 years. Our products are positioned for mass market with other competitive brands such as Balmora, Pelvaxo, Quorel, and Lumiva, to give you a better understanding of the category. What we are looking for in our packaging is an ethical, pharmaceutical look that will appeal to mothers as a product that is safe and effective for their baby. The packaging should be clean, fresh, and consumer friendly, while still maintaining that this is a clinical product. The design concepts are a box design for the Diaper Rash Cream and a plastic packaging design for the Diaper Wipes. Attached you will find the Mavory logo and examples of Diaper Rash Cream box packaging and Diaper Wipes plastic packaging from competitors (to give you an idea of what shape of packaging we like). Please feel free to contact me should you have any questions.Thank you for your time and effort,Roska

Target Market(s)

We are a mid – premium priced brand with a focus on targeting mothers between the ages of 18 – 35 years.

Industry/Entity Type

Baby Care

Requirements
Must have
• Packaging design concepts for a box design for the Diaper Rash Cream and a plastic packaging design for the Diaper Wipes.
Nice to have
• Diaper Rash Cream box: 8 cm width, 8 cm length, 8 cm depth
• Diaper Wipes package: 23 cm width, 10.5 cm length, 4.5 cm depth

```html
<!DOCTYPE html>
<html lang="en">
<head>
<meta charset="utf-8">
<title>Mavory Fragrance-Free Baby Wipes – Pack Front</title>
<link rel="stylesheet" href="https://fonts.googleapis.com/css2?family=Nunito:wght@300;400;800;900&display=swap">
<style>
  :root {
    --page: #ffffff;
    --deep-blue: #123f9e;
    --mid-blue: #2a66c8;
    --bright-blue: #3f8fe0;
    --teal: #4db8c6;
    --white: #ffffff;
  }
  * { margin: 0; padding: 0; box-sizing: border-box; }
  html, body {
    width: 1200px;
    height: 702px;
    overflow: hidden;
    background: var(--page);
  }
  .canvas {
    position: relative;
    width: 1200px;
    height: 702px;
    background: var(--page);
    font-family: "Nunito", Arial, sans-serif;
  }
  .pack-front {
    position: absolute;
    left: 136px;
    top: 112px;
    width: 943px;
    height: 430px;
    overflow: hidden;
  }
  .water-photo {
    position: absolute;
    inset: 0;
    background:
      radial-gradient(ellipse at 80% 45%, rgba(120, 190, 240, 0.55), transparent 55%),
      radial-gradient(ellipse at 50% 90%, rgba(70, 140, 220, 0.45), transparent 60%),
      linear-gradient(100deg, var(--deep-blue) 0%, var(--mid-blue) 45%, var(--bright-blue) 100%);
  }
  .brand-name {
    position: absolute;
    left: 664px;
    top: 88px;
    width: 244px;
    text-align: center;
    color: var(--white);
    font-weight: 900;
    font-size: 40px;
    letter-spacing: 2px;
    text-transform: uppercase;
    line-height: 1;
  }
  .variant {
    position: absolute;
    left: 104px;
    top: 116px;
    color: var(--white);
    font-weight: 300;
    font-size: 40px;
    letter-spacing: -0.5px;
    line-height: 1;
  }
  .product-name {
    position: absolute;
    left: 98px;
    top: 168px;
    font-weight: 900;
    font-size: 118px;
    line-height: 1;
    letter-spacing: -3px;
    white-space: nowrap;
  }
  .product-name .word-baby { color: var(--white); }
  .product-name .word-wipes {
    color: var(--teal);
    -webkit-text-stroke: 4px var(--white);
    paint-order: stroke fill;
  }
  .claim-line {
    position: absolute;
    left: 26px;
    top: 386px;
    display: flex;
    align-items: baseline;
    gap: 14px;
    color: var(--white);
    white-space: nowrap;
  }
  .claim-line .water-content {
    font-weight: 900;
    font-size: 29px;
    letter-spacing: -0.5px;
  }
  .claim-line .safety-claim {
    font-weight: 400;
    font-size: 20.5px;
    letter-spacing: -0.4px;
  }
</style>
</head>
<body>
  <div class="canvas">
    <section class="pack-front">
      <div class="water-photo" role="img" aria-label="Close-up photograph of water droplets on a blue surface"></div>
      <div class="brand-name">Mavory</div>
      <p class="variant">Fragrance-Free</p>
      <h1 class="product-name"><span class="word-baby">Baby</span><span class="word-wipes">Wipes</span></h1>
      <p class="claim-line">
        <span class="water-content">91.2% Water</span>
        <span class="safety-claim">Clincally Tested And Proven As Safe As Pure Water On Newborn Skin</span>
      </p>
    </section>
  </div>
</body>
</html>
```